Designer Instructions – Updated Referral Program Flyer

(Based on the mock-up in “Brief Layout and Instructions.pdf”)

OVERALL STYLE + LAYOUT

Maintain the same general layout, structure, and flow as the mock-up flyer (front and back).

This is an update of an older flyer, not a full redesign — keep the same sections, proportions, and overall visual feel, but with cleaner, more modern design improvements.

The final flyer should look clean, bold, professional, and high-impact, geared toward realtors, property managers, and contractors who refer work.

FRONT SIDE INSTRUCTIONS
1. Header Section

Remove the Tallow Ridge Builders logo from the top banner.
(Shown on page 1 of the PDF)

2. Main Headline

Keep the same three-line structure:
EARN
UNLIMITED
CASH

Center it, maximize impact, and increase the font size of CASH so all three words match in importance.

Make the headline bold, clean, and the main focal point.

3. Cash Incentive Box

Keep the "$500 minimum OR 10% per referral" box, but upgrade the graphics to look sharper and more modern.

Ensure the wording matches exactly what’s in the mock-up.

4. Premier Partner Program Ribbon

Clean up and modernize the "PREMIER PARTNER PROGRAM" bar while keeping the same position and structure.

Ensure the checkmark badge remains crisp and professional.

5. Supporting Icons Section

Keep the four icons/benefit boxes (Guaranteed Payout, Free Evaluations, Affordable Solutions, Industry Leaders) in the same order.

Update the icons to cleaner, more modern styles — but maintain the same meanings.

Improve alignment and spacing for sharper visual consistency.

6. Remove Icons in Contact Area

At the bottom (“CALL TEXT OR BOOK ONLINE 555-014-2796 TallowRidgeBuilders.example”), remove the phone and internet icons, as noted on page 2 of the PDF.

7. Replace All Images

I (Darnell) will provide all updated stock images separately via email.

Replace the flood/water-damage imagery and roof leak with the new images I send.

Keep image placement and proportions the same as the mock-up.

BACK SIDE INSTRUCTIONS
1. Header Image + “REFER / EARN” Section

Maintain the same large split-image layout (“The more you refer, the more you earn”).

Replace all background imagery with the new assets I will send.

Keep the CASH FLOW image section but modernize the type and spacing.

2. “HOW IT WORKS” Section

Preserve the three-column layout:

Refer Flood, Water & Mold Damage

We Take Care of Everything (evaluations/insurance)

Get Paid to Share

Update images, tighten spacing, and use modern iconography.

3. Remove Phone/Internet Icons

Same as the front side — remove small communication icons and keep only the text/number/URL.

4. Bottom Contact Bar

Keep the blue bar, same wording, same layout — just modernize the style if needed for clarity.

5. Replace All Back-Side Images

Again, I will email you the image assets.

Keep the layout EXACT — just update with higher-quality photos and improved design.

TEXT CONTENT (Keep as-is unless spacing adjustments needed)

All text shown in the PDF should remain exactly the same unless spacing or visual balance requires minor adjustments.
Example from page 3:

“REFER FLOOD, MOLD & CONSTRUCTION JOBS”

“We Schedule a Free Estimate. If Approved, You Get Paid.”

“Everybody Benefits From Referrals”

Everything stays, just refreshed and visually improved.

DESIGN GOALS

Flyer should look high-end and trustworthy, not salesy.

Consistent color theme: blues, whites, yellows, same palette as original.

Use bold, modern fonts with strong readability.

Ensure all headlines pop and all benefit boxes are clean, well-aligned, and evenly spaced.

The final result should feel like a premium referral program flyer for a top-tier restoration/remodel company.

FILES I WILL PROVIDE

I will send the designer:

All replacement stock photos

Any updated logos (if needed)

Original high-resolution version of the mock-up (if available)

Any additional icons preferred

0054AA
0677BA
7BADD7
CADEEF
E8F1F8

• Designer Instructions – Updated Referral Program Flyer (Based on the mock-up in “Brief Layout and Instructions.pdf”) OVERALL STYLE + LAYOUT Maintain the same general layout, structure, and flow as the mock-up flyer (front and back). This is an update of an older flyer, not a full redesign — keep the same sections, proportions, and overall visual feel, but with cleaner, more modern design improvements. The final flyer should look clean, bold, professional, and high-impact, geared toward realtors, property managers, and contractors who refer work. FRONT SIDE INSTRUCTIONS 1. Header Section Remove the Tallow Ridge Builders logo from the top banner. (Shown on page 1 of the PDF) 2. Main Headline Keep the same three-line structure: EARN UNLIMITED CASH Center it, maximize impact, and increase the font size of CASH so all three words match in importance. Make the headline bold, clean, and the main focal point. 3. Cash Incentive Box Keep the "$500 minimum OR 10% per referral" box, but upgrade the graphics to look sharper and more modern. Ensure the wording matches exactly what’s in the mock-up. 4. Premier Partner Program Ribbon Clean up and modernize the "PREMIER PARTNER PROGRAM" bar while keeping the same position and structure. Ensure the checkmark badge remains crisp and professional. 5. Supporting Icons Section Keep the four icons/benefit boxes (Guaranteed Payout, Free Evaluations, Affordable Solutions, Industry Leaders) in the same order. Update the icons to cleaner, more modern styles — but maintain the same meanings. Improve alignment and spacing for sharper visual consistency. 6. Remove Icons in Contact Area At the bottom (“CALL TEXT OR BOOK ONLINE 555-014-2796 TallowRidgeBuilders.example”), remove the phone and internet icons, as noted on page 2 of the PDF. 7. Replace All Images I (Darnell) will provide all updated stock images separately via email. Replace the flood/water-damage imagery and roof leak with the new images I send. Keep image placement and proportions the same as the mock-up. BACK SIDE INSTRUCTIONS 1. Header Image + “REFER / EARN” Section Maintain the same large split-image layout (“The more you refer, the more you earn”). Replace all background imagery with the new assets I will send. Keep the CASH FLOW image section but modernize the type and spacing. 2. “HOW IT WORKS” Section Preserve the three-column layout: Refer Flood, Water & Mold Damage We Take Care of Everything (evaluations/insurance) Get Paid to Share Update images, tighten spacing, and use modern iconography. 3. Remove Phone/Internet Icons Same as the front side — remove small communication icons and keep only the text/number/URL. 4. Bottom Contact Bar Keep the blue bar, same wording, same layout — just modernize the style if needed for clarity. 5. Replace All Back-Side Images Again, I will email you the image assets. Keep the layout EXACT — just update with higher-quality photos and improved design. TEXT CONTENT (Keep as-is unless spacing adjustments needed) All text shown in the PDF should remain exactly the same unless spacing or visual balance requires minor adjustments. Example from page 3: “REFER FLOOD, MOLD & CONSTRUCTION JOBS” “We Schedule a Free Estimate. If Approved, You Get Paid.” “Everybody Benefits From Referrals” Everything stays, just refreshed and visually improved. DESIGN GOALS Flyer should look high-end and trustworthy, not salesy. Consistent color theme: blues, whites, yellows, same palette as original. Use bold, modern fonts with strong readability. Ensure all headlines pop and all benefit boxes are clean, well-aligned, and evenly spaced. The final result should feel like a premium referral program flyer for a top-tier restoration/remodel company. FILES I WILL PROVIDE I will send the designer: All replacement stock photos Any updated logos (if needed) Original high-resolution version of the mock-up (if available) Any additional icons preferred

```html
<!DOCTYPE html>
<html lang="en">
<head>
<meta charset="utf-8">
<title>Referral Partner Program Flyer</title>
<link href="https://fonts.googleapis.com/css2?family=Anton&family=Poppins:wght@400;500;600;700;800;900&display=swap" rel="stylesheet">
<style>
:root{
  --stage:#808080;
  --navy:#0d2f7a;
  --navy-deep:#0a1a3a;
  --blue:#1b3f94;
  --royal:#0054AA;
  --sky:#7BADD7;
  --red:#c8101e;
  --red-deep:#a50c17;
  --yellow:#ffe500;
  --orange:#ff9a1a;
  --grey:#d4d4d4;
  --grey-dark:#4a4a4a;
  --ink:#222;
  --white:#fff;
}
*{box-sizing:border-box;margin:0;padding:0}
html,body{width:913px;height:1200px;overflow:hidden}
body{background:var(--stage);font-family:"Poppins",sans-serif;position:relative}
.card{position:absolute;left:96px;width:721px;height:466px;background:var(--white);overflow:hidden;box-shadow:0 4px 10px rgba(0,0,0,.25)}
.card--front{top:89px}
.card--back{top:628px}
.abs{position:absolute}
.header-art{position:absolute;left:0;top:0;width:721px;height:222px}

/* front headline */
.headline{position:absolute;left:0;top:24px;width:354px;text-align:center;font-weight:900;line-height:.86;letter-spacing:-1px}
.headline .earn{display:block;color:var(--yellow);font-size:96px}
.headline .unlimited{display:block;color:var(--white);font-size:54px;margin-top:6px}
.headline .cash{display:block;color:var(--white);font-size:54px;margin-top:6px}

/* incentive ribbon */
.incentive{position:absolute;left:33px;top:226px;width:361px;height:50px}
.incentive svg{position:absolute;inset:0}
.incentive .amount{position:absolute;left:28px;top:2px;color:var(--white);font-weight:800;font-size:29px;line-height:1}
.incentive .amount sup{font-size:14px;vertical-align:top;position:relative;top:3px}
.incentive .minimum{position:absolute;left:28px;top:30px;color:var(--yellow);font-weight:700;font-size:14px;line-height:1}
.incentive .or{position:absolute;left:111px;top:2px;width:46px;height:46px;border-radius:50%;background:var(--red);border:2px solid var(--white);color:var(--white);font-weight:600;font-size:17px;display:flex;align-items:center;justify-content:center}
.incentive .pct{position:absolute;left:168px;top:4px;color:var(--white);font-weight:800;font-size:36px;line-height:1}
.incentive .per{position:absolute;left:247px;top:5px;color:var(--yellow);font-weight:800;font-size:18px;line-height:.95}

/* partner ribbon */
.premier-tab{position:absolute;left:479px;top:225px;width:140px;height:21px}
.premier-tab span{position:absolute;inset:0;color:var(--white);font-weight:700;font-size:15px;letter-spacing:3px;text-align:center;line-height:21px}
.partner-pill{position:absolute;left:412px;top:246px;width:289px;height:30px;border-radius:8px;background:linear-gradient(90deg,var(--red) 0 47%,var(--grey-dark) 47%);display:flex;align-items:center;justify-content:space-between;padding:0 10px;color:var(--white);font-weight:700;font-size:21px}
.partner-pill .shield{position:absolute;left:122px;top:-2px;width:34px;height:34px;border-radius:50%;background:var(--red);border:2px solid var(--white);display:flex;align-items:center;justify-content:center}

.tagline{position:absolute;left:0;width:721px;top:284px;text-align:center;color:var(--navy);font-weight:800;font-size:21px;letter-spacing:-.3px}

/* benefits */
.benefit{position:absolute;top:318px;width:140px;height:75px}
.benefit .frame{position:absolute;left:0;top:3px;width:128px;height:72px;border:2px solid var(--navy);border-top:none;border-radius:0 0 0 8px}
.benefit .label{position:absolute;left:0;top:0;width:118px;height:30px;background:var(--navy);border-radius:8px 8px 0 0;padding:3px 0 0 4px}
.benefit .label span{display:block;background:var(--white);border-radius:6px 0 0 6px;height:24px;padding:2px 0 0 7px;color:var(--navy);font-weight:700;font-size:9.5px;line-height:.95}
.benefit .icon{position:absolute;left:104px;top:-3px;width:36px;height:36px;border-radius:50%;background:var(--navy);display:flex;align-items:center;justify-content:center}
.benefit p{position:absolute;left:10px;top:37px;width:120px;font-size:8.4px;line-height:1.28;color:var(--ink);font-weight:500}
.benefit p b{font-weight:700;color:var(--navy)}
.badge-24{position:absolute;left:624px;top:319px;width:76px;height:66px}

.slogan{position:absolute;left:0;width:721px;top:400px;text-align:center;font-weight:800;font-size:21px;color:var(--navy);letter-spacing:-.3px}
.slogan em{font-style:normal;color:var(--red)}

/* contact bar */
.contact{position:absolute;left:0;top:430px;width:721px;height:36px;background:var(--grey)}
.contact svg{position:absolute;left:0;top:0}
.contact .cta{position:absolute;left:39px;top:0;line-height:36px;color:var(--white);font-weight:700;font-size:15px;letter-spacing:-.2px}
.contact .phone{position:absolute;left:315px;top:0;line-height:36px;color:#333;font-weight:600;font-size:17px}
.contact .divider{position:absolute;left:451px;top:6px;width:1px;height:24px;background:#888}
.contact .web{position:absolute;left:462px;top:0;line-height:36px;color:#333;font-size:13.5px}
.contact .web b{font-weight:600}

/* back */
.slogan-stack{position:absolute;left:62px;top:16px;width:154px;font-family:"Anton",sans-serif;line-height:.98;text-align:center;text-transform:uppercase}
.slogan-stack .small{display:block;color:var(--white);font-size:27px}
.slogan-stack .big{display:block;font-size:60px;line-height:.95;background:linear-gradient(180deg,var(--yellow) 30%,var(--orange));-webkit-background-clip:text;background-clip:text;color:transparent}
.slogan-stack .big--earn{font-size:74px}
.how-band{position:absolute;left:0;top:219px;width:251px;height:31px}
.how-band span{position:absolute;left:58px;top:0;line-height:31px;color:var(--navy);font-weight:800;font-size:20px}
.step{position:absolute;top:263px;width:156px;height:152px;border:2px solid var(--ink);border-radius:10px;overflow:hidden;background:var(--white)}
.step .photo{height:74px;border-bottom:3px solid var(--royal)}
.step h3{margin-top:10px;text-align:center;color:var(--navy);font-weight:800;font-size:10.5px;line-height:1.1}
.step p{margin-top:3px;text-align:center;font-size:8.8px;line-height:1.3;color:var(--ink)}
.refer-list{position:absolute;left:530px;top:245px;width:160px;text-align:center;font-weight:800;font-size:16px;line-height:1.02;color:#1e2a44}
.refer-list .lead{color:var(--navy)}
.service-badge{position:absolute;left:539px;top:332px;width:147px;height:70px;background:var(--blue);border-top:12px solid var(--red);border-bottom:6px solid var(--navy-deep)}
</style>
</head>
<body>

<!-- FRONT -->
<section class="card card--front">
  <svg class="header-art" viewBox="0 0 721 222" aria-hidden="true">
    <defs>
      <linearGradient id="frontBlue" x1="0" y1="0" x2="0" y2="1">
        <stop offset="0" stop-color="#1a3c92"/><stop offset="1" stop-color="#152f74"/>
      </linearGradient>
    </defs>
    <rect width="721" height="222" fill="url(#frontBlue)"/>
    <polygon points="368,0 412,0 354,109 415,222 380,222 330,109" fill="#0b49c6"/>
  </svg>
  <div class="abs" role="img" aria-label="Air movers and dehumidifiers drying a finished basement" style="left:0;top:0;width:721px;height:222px;clip-path:polygon(412px 0,721px 0,721px 222px,415px 222px,354px 109px);background:linear-gradient(135deg,#c9c6c0 0%,#a9a59d 45%,#4fa3cf 70%,#6d6b66 100%)"></div>
  <div class="abs" style="left:0;top:0;width:721px;height:222px;clip-path:polygon(410px 0,414px 0,356px 109px,417px 222px,413px 222px,352px 109px);background:var(--white)"></div>

  <h1 class="headline">
    <span class="earn">EARN</span>
    <span class="unlimited">UNLIMITED</span>
    <span class="cash">CASH</span>
  </h1>

  <div class="incentive">
    <svg viewBox="0 0 361 50" width="361" height="50" aria-hidden="true">
      <polygon points="14,0 350,0 361,50 0,50" fill="var(--red)"/>
      <polygon points="14,0 110,0 100,50 0,50" fill="var(--red-deep)"/>
    </svg>
    <div class="amount"><sup>$</sup>500</div>
    <div class="minimum">MINIMUM</div>
    <div class="or">OR</div>
    <div class="pct">10%</div>
    <div class="per">PER<br>REFERRAL</div>
  </div>

  <div class="premier-tab">
    <svg viewBox="0 0 140 21" width="140" height="21" aria-hidden="true"><polygon points="8,0 132,0 140,21 0,21" fill="var(--navy)"/></svg>
    <span>PREMIER</span>
  </div>
  <div class="partner-pill">
    <span>PARTNER</span>
    <span class="shield">
      <svg width="18" height="20" viewBox="0 0 18 20" aria-hidden="true"><path d="M9 1 L17 4 V10 C17 15 13 18 9 19 C5 18 1 15 1 10 V4 Z" fill="var(--white)"/><path d="M5 10 L8 13 L13 7" fill="none" stroke="var(--red)" stroke-width="2.4" stroke-linecap="round" stroke-linejoin="round"/></svg>
    </span>
    <span>PROGRAM</span>
  </div>

  <p class="tagline">PARTNER WITH US &amp; EVERYBODY WINS!</p>

  <div class="benefit" style="left:33px">
    <div class="frame"></div>
    <div class="label"><span>GUARANTEED<br>PAYOUT</span></div>
    <div class="icon"><svg width="24" height="24" viewBox="0 0 24 24" aria-hidden="true"><circle cx="12" cy="12" r="10" fill="none" stroke="#fff" stroke-width="2"/><path d="M7 12 L10.5 15.5 L17 9" fill="none" stroke="#fff" stroke-width="2.4" stroke-linecap="round" stroke-linejoin="round"/></svg></div>
    <p>Minimum <b>$500</b> or<br><b>10%</b> of Total Invoice<br>Paid Fast</p>
  </div>
  <div class="benefit" style="left:183px">
    <div class="frame"></div>
    <div class="label"><span>FREE<br>ESTIMATES</span></div>
    <div class="icon"><svg width="22" height="22" viewBox="0 0 22 22" aria-hidden="true"><rect x="4" y="2" width="13" height="17" rx="1.5" fill="none" stroke="#fff" stroke-width="1.8"/><path d="M7 7h7M7 10h7M7 13h4" stroke="#fff" stroke-width="1.5"/><circle cx="17" cy="17" r="4" fill="#fff"/><path d="M15 17l1.5 1.5L19 15.5" fill="none" stroke="var(--navy)" stroke-width="1.5"/></svg></div>
    <p><b>Fast &amp; Free<br>Inspections</b> &amp; Written<br>Estimates</p>
  </div>
  <div class="benefit" style="left:332px">
    <div class="frame"></div>
    <div class="label"><span>AFFORDABLE<br>SOLUTIONS</span></div>
    <div class="icon"><svg width="22" height="22" viewBox="0 0 22 22" aria-hidden="true"><circle cx="12" cy="9" r="6" fill="none" stroke="#fff" stroke-width="1.8"/><text x="12" y="12.5" text-anchor="middle" font-family="Poppins,sans-serif" font-weight="700" font-size="9" fill="#fff">$</text><path d="M2 17 L7 15 L12 17 L19 15" fill="none" stroke="#fff" stroke-width="1.8" stroke-linecap="round"/></svg></div>
    <p><b>Lowest</b> Out of<br><b>Pocket Costs</b> for Your<br>Customers</p>
  </div>
  <div class="benefit" style="left:481px">
    <div class="frame"></div>
    <div class="label"><span>INDUSTRY<br>LEADERS</span></div>
    <div class="icon"><svg width="24" height="22" viewBox="0 0 24 22" aria-hidden="true"><circle cx="12" cy="5" r="3" fill="none" stroke="#fff" stroke-width="1.6"/><circle cx="5" cy="14" r="2.2" fill="#fff"/><circle cx="12" cy="14" r="2.2" fill="#fff"/><circle cx="19" cy="14" r="2.2" fill="#fff"/><path d="M2 21c0-3 6-3 6 0M9 21c0-3 6-3 6 0M16 21c0-3 6-3 6 0" fill="none" stroke="#fff" stroke-width="1.4"/></svg></div>
    <p><b>Licensed &amp; Certified</b><br>Experts Provide<br><b>100% Guarantee</b></p>
  </div>
  <svg class="badge-24" viewBox="0 0 76 66" role="img" aria-label="Emergency service badge">
    <circle cx="38" cy="33" r="31" fill="none" stroke="var(--red)" stroke-width="4"/>
    <circle cx="38" cy="33" r="21" fill="var(--red)"/>
  </svg>

  <p class="slogan">SEND <em>REFERRALS.</em> GET <em>PAID.</em> GROW <em>YOUR BUSINESS.</em></p>

  <div class="contact">
    <svg width="300" height="36" viewBox="0 0 300 36" aria-hidden="true"><polygon points="0,0 285,0 294,18 285,36 0,36" fill="var(--navy)"/><polygon points="285,0 290,0 299,18 290,36 285,36 294,18" fill="var(--white)"/></svg>
    <span class="cta">CALL, TEXT OR BOOK ONLINE</span>
    <span class="phone">555-014-2796</span>
    <span class="divider"></span>
    <span class="web">www.<b>TallowRidgeBuilders</b>.example</span>
  </div>
</section>

<!-- BACK -->
<section class="card card--back">
  <svg class="header-art" viewBox="0 0 721 222" aria-hidden="true">
    <rect width="721" height="222" fill="var(--blue)"/>
    <polygon points="0,222 359,222 318,70 180,30 60,150" fill="var(--navy-deep)"/>
  </svg>
  <div class="abs" role="img" aria-label="Hundred dollar bills with letter tiles spelling cash flow" style="left:0;top:0;width:721px;height:222px;clip-path:polygon(300px 0,721px 0,721px 222px,359px 222px);background:linear-gradient(135deg,#d9d8d0 0%,#b8b9ad 40%,#9fe0e0 55%,#c7c6bb 75%,#8f9188 100%)"></div>

  <div class="slogan-stack">
    <span class="small">THE MORE YOU</span>
    <span class="big">REFER</span>
    <span class="small">THE MORE YOU</span>
    <span class="big big--earn">EARN</span>
  </div>

  <div class="how-band">
    <svg width="251" height="31" viewBox="0 0 251 31" aria-hidden="true"><polygon points="0,0 241,0 251,31 0,31" fill="var(--yellow)"/></svg>
    <span>HOW IT WORKS</span>
  </div>

  <article class="step" style="left:38px">
    <div class="photo" role="img" aria-label="Thermal camera scanning a wall for moisture" style="background:linear-gradient(90deg,#e8e4dc 0%,#cfc6b8 50%,#d93c6a 72%,#f08a2a 100%)"></div>
    <h3>REFER FLOOD, MOLD &amp;<br>CONSTRUCTION JOBS</h3>
    <p>It's Simple to Refer 24/7:<br>Call, Text or Book Online.</p>
  </article>
  <article class="step" style="left:202px">
    <div class="photo" role="img" aria-label="Inspector with a clipboard in front of a house" style="background:linear-gradient(90deg,#8fb0d6 0%,#cfd8e2 50%,#7c8f5e 80%,#5a7040 100%)"></div>
    <h3>WE TAKE CARE OF<br>EVERYTHING:</h3>
    <p>We Schedule a Free Estimate.<br>If Approved, You Get Paid.</p>
  </article>
  <article class="step" style="left:368px">
    <div class="photo" role="img" aria-label="Yellow road sign reading get paid to share against a blue sky" style="background:linear-gradient(90deg,#6ea2d8 0%,#b8d2ec 55%,#f2d900 78%,#7aa8dc 100%)"></div>
    <h3>EVERYBODY BENEFITS<br>FROM REFERRALS</h3>
    <p>We Provide Expert Quality<br>Work for Affordable Price.</p>
  </article>

  <p class="refer-list"><span class="lead">REFER:</span><br>FLOODS,<br>REMODELS,<br>RENOVATIONS<br>&amp; REPAIRS</p>
  <div class="service-badge" role="img" aria-label="Emergency repair services badge"></div>

  <div class="contact">
    <svg width="300" height="36" viewBox="0 0 300 36" aria-hidden="true"><polygon points="0,0 285,0 294,18 285,36 0,36" fill="var(--navy)"/><polygon points="285,0 290,0 299,18 290,36 285,36 294,18" fill="var(--white)"/></svg>
    <span class="cta">CALL, TEXT OR BOOK ONLINE</span>
    <span class="phone">555-014-2796</span>
    <span class="divider"></span>
    <span class="web">www.<b>TallowRidgeBuilders</b>.example</span>
  </div>
</section>

</body>
</html>
```